Give Bright Oak an Online Presence!

Bright Oak Property Maintenance is an Australian Owned property maintenance company who needs a stand out online presence.

BOK maintains many buildings and sites and wants to appeal to a corporate professional market with their brand new website. BOK is essentially a handyman service offering all maintenance services to home owners, office managers, real estate agents and strata managers.

The Website:
We need a corporate website that appeals to our broader customer base (property owners, property managers, office managers) the copy is being written by a professional so use filler text for now.

Things that we want:
Home page that sets us apart and appeals to the corporate and residential market. The home page needs to not focus on either the residential or commercial market. The home page should focus on our logo and branding. We have a logo already and it is attached to the brief, please use it and try to consider the colour pallette that goes with it. Whilst we want the site to appear strong and manly it is important to remember that 95% of our customers are female so we need the site to be appealing to women. Women need to believe that we are strong, dependable and trustworthy.
We'd like a quote page and potentially also the ability to get a quote from the home page (please don't put it in if it ruins the overall feel of the home page)
An "about us" page
A contact us page
A blog that's built in (we don't want to link to an external blog)
(overall we'd expect to have 6 or 7 pages total)

The site will also need coding - we expect this to be done in a separate project but need you to consider a few things about the coding side of things.

It needs to be iPhone and iPad compatible.

We'd like you to suggest the best CMS that you would use or if you would suggest not using a CMS please let us know with your submissions.

Target Market(s)

Property owners, office managers and property managers who need maintenance on buildings (So all of them)

Industry/Entity Type

Property Maintenance

Requirements
Must have
• Our Logo
Home page
About Us
Residential
Commercial
Real Estate/Strata
Contact Us/Quote
Blog
Nice to have
• Quote form included in home page
Movement on the home page at least
Should not have
• other logos, too much colour
NO FLASH

```html
<!DOCTYPE html>
<html lang="en">
<head>
<meta charset="utf-8">
<title>Bright Oak Property Maintenance</title>
<link rel="stylesheet" href="https://fonts.googleapis.com/css2?family=Arimo:ital,wght@0,400;0,700;1,400&display=swap">
<style>
  :root {
    --orange: #f08a1c;
    --orange-light: #f6a22e;
    --orange-deep: #e27712;
    --charcoal: #4b4b4b;
    --charcoal-dark: #3a3a3a;
    --nav-text: #333333;
    --blue: #1b7cc2;
    --body-text: #555555;
    --rule: #777777;
    --white: #ffffff;
  }
  * { box-sizing: border-box; margin: 0; padding: 0; }
  html, body { width: 1200px; height: 600px; overflow: hidden; background: var(--white); }
  body { font-family: "Arimo", Arial, sans-serif; position: relative; }

  .top-strip { position: absolute; left: 120px; top: 0; width: 960px; height: 18px;
    background: linear-gradient(90deg, var(--orange-light) 0, var(--orange) 70%, var(--charcoal) 71%); }
  .top-strip svg { position: absolute; left: 0; top: 0; }

  .main-nav { position: absolute; left: 120px; top: 18px; width: 792px; height: 42px;
    background: linear-gradient(#ffffff, #f1f1f1); display: flex; }
  .main-nav a { display: flex; align-items: center; justify-content: center; height: 100%;
    font-size: 12px; color: var(--nav-text); text-decoration: none; letter-spacing: -0.2px;
    border-right: 1px solid #d8d8d8; }
  .main-nav a.is-current { color: var(--orange); background: #fafafa; }
  .main-nav a:last-child { border-right: 0; }
  .badge-new { background: var(--blue); color: var(--white); font-size: 9px; font-weight: 700;
    border-radius: 8px; padding: 2px 5px; margin-right: 8px; }

  .search-area { position: absolute; left: 912px; top: 18px; width: 168px; height: 42px; background: #f3f3f3; }
  .search-field { position: absolute; left: 9px; top: 7px; width: 125px; height: 27px; background: var(--white);
    border: 1px solid #cfcfcf; font-size: 11px; font-style: italic; color: #444; padding: 7px 8px; }
  .search-icon { position: absolute; left: 144px; top: 13px; }

  .hero { position: absolute; left: 120px; top: 60px; width: 960px; height: 244px; overflow: hidden;
    background: var(--charcoal); }
  .hero-shape { position: absolute; left: 0; top: 0; }
  .crew-placeholder { position: absolute; left: 40px; top: 28px; width: 180px; height: 140px;
    background: linear-gradient(180deg, #3a2a1c 0%, #5a3a1c 100%); opacity: .85; border-radius: 4px; }
  .brand-name { position: absolute; left: 25px; top: 178px; width: 240px; text-align: center;
    color: var(--white); font-weight: 700; font-size: 17px; line-height: 20px; text-transform: uppercase; }

  .hero-headline { position: absolute; left: 272px; top: 56px; color: var(--white); }
  .hero-headline h1 { font-size: 90px; font-weight: 700; line-height: 80px; letter-spacing: -1px; }
  .hero-headline .tagline { font-size: 18px; font-weight: 700; text-transform: uppercase; margin-top: 4px; }
  .hero-headline .tagline-sub { font-size: 16px; font-style: italic; text-transform: uppercase; color: #fde4c6; }

  .quote-card { position: absolute; left: 720px; top: 23px; width: 214px; height: 122px;
    background: #2e2e2e; border-radius: 6px; padding: 7px; }
  .quote-card::after { content: ""; position: absolute; left: 96px; bottom: -10px;
    border: 8px solid transparent; border-top-color: #2e2e2e; border-bottom: 0; }
  .quote-inner { background: linear-gradient(#ffffff, #c9c9c9); border-radius: 4px; height: 100%; padding: 6px 13px; }
  .quote-inner h2 { font-size: 11px; font-weight: 700; text-align: center; color: #333; margin-bottom: 7px; }
  .quote-field { height: 29px; background: var(--white); border: 1px solid #d0d0d0; border-radius: 5px;
    font-size: 11px; font-style: italic; color: #666; padding: 8px 9px; margin-bottom: 8px; }
  .quote-button { position: absolute; left: 723px; top: 182px; width: 201px; height: 34px;
    background: linear-gradient(#fbb443, var(--orange-deep)); border-radius: 17px; color: var(--white);
    font-weight: 700; font-size: 16px; text-align: center; line-height: 34px; }

  .hero-shadow { position: absolute; left: 150px; top: 304px; width: 900px; height: 14px;
    background: radial-gradient(ellipse at top, rgba(0,0,0,.22), rgba(0,0,0,0) 70%); }

  .content { position: absolute; left: 119px; top: 335px; width: 955px; }
  .content h2.section-title { font-size: 32px; font-weight: 400; color: var(--blue); line-height: 34px; }
  .body-copy { font-size: 12px; line-height: 15px; color: var(--body-text); text-align: justify;
    height: 45px; overflow: hidden; }
  .about-copy { margin-top: 21px; }
  .divider { display: flex; align-items: center; margin: 16px -3px 15px; }
  .divider::before, .divider::after { content: ""; flex: 1; height: 2px; background: var(--rule); }
  .divider h3 { font-size: 24px; font-weight: 400; color: #777; padding: 0 20px; line-height: 28px; }
  .footer-rule { position: absolute; left: 117px; top: 570px; width: 960px; height: 1px; background: #cccccc; }
</style>
</head>
<body>
  <div class="top-strip">
    <svg width="960" height="18" viewBox="0 0 960 18" aria-hidden="true">
      <rect width="960" height="18" fill="#4b4b4b"/>
      <path d="M0 0 H672 Q682 2 686 18 H0 Z" fill="#f08a1c"/>
    </svg>
  </div>

  <nav class="main-nav">
    <a href="#" class="is-current" style="width:70px">START</a>
    <a href="#" style="width:97px">ABOUT US</a>
    <a href="#" style="width:110px">RESIDENTIAL</a>
    <a href="#" style="width:109px">COMMERCIAL</a>
    <a href="#" style="width:155px">REAL ESTATE/STRATA</a>
    <a href="#" style="width:150px">CONTACT US/QUOTE</a>
    <a href="#" style="width:101px"><span class="badge-new">NEW</span>BLOG</a>
  </nav>

  <div class="search-area">
    <div class="search-field">Search...</div>
    <svg class="search-icon" width="14" height="14" viewBox="0 0 14 14" aria-hidden="true">
      <circle cx="5.5" cy="5.5" r="4.3" fill="none" stroke="#1b7cc2" stroke-width="2"/>
      <line x1="8.7" y1="8.7" x2="13" y2="13" stroke="#1b7cc2" stroke-width="2.2" stroke-linecap="round"/>
    </svg>
  </div>

  <section class="hero">
    <svg class="hero-shape" width="960" height="244" viewBox="0 0 960 244" aria-hidden="true">
      <defs>
        <linearGradient id="heroOrange" x1="0" y1="0" x2="1" y2="1">
          <stop offset="0" stop-color="#f6a22e"/>
          <stop offset="1" stop-color="#e87e14"/>
        </linearGradient>
      </defs>
      <rect width="960" height="244" fill="#4b4b4b"/>
      <path d="M0 0 H686 C700 40 692 70 670 110 C645 155 640 200 652 244 H0 Z" fill="url(#heroOrange)"/>
    </svg>
    <div class="crew-placeholder" role="img" aria-label="Silhouettes of three tradesmen standing above a city skyline"></div>
    <div class="brand-name">Bright Oak<br>Property Maintenance</div>

    <div class="hero-headline">
      <h1>SIMPLY</h1>
      <p class="tagline">The best property maintenance</p>
      <p class="tagline-sub">You can get anywhere</p>
    </div>

    <form class="quote-card">
      <div class="quote-inner">
        <h2>Request a quote now!</h2>
        <div class="quote-field">Your E-mail</div>
        <div class="quote-field">Your Property type</div>
      </div>
    </form>
    <div class="quote-button">REQUEST QUOTE</div>
  </section>
  <div class="hero-shadow"></div>

  <main class="content">
    <h2 class="section-title">ABOUT US</h2>
    <p class="body-copy about-copy">Lorem ipsum dolor sit amet, consectetur adipisicing elit. Proin nibh augue, suscipit a, scelerisque sed, lacinia in, mi. Cras vel lorem. Etiam pellentesque aliquetLorem ipsum dolor sit amet, consectetur adipisicing elit. Proin nibh augue, suscipit a, scelerisque sed, lacinia in, mi. Cras vel lorem. Etiam pellentesque aliquetLorem ipsum dolor sit amet, consectetur adipisicing elit. Proin nibh augue, suscipit a, scelerisque sed, lacinia in, mi. Cras vel lorem. Etiam pellentesque aliquetLorem ipsum dolor sit amet, consectetur adipisicing elit. Proin nibh augue, suscipit a, scelerisque sed.</p>
    <div class="divider"><h3>LOREM IPSUM DOLOR SIT AM CONTESTADUR</h3></div>
    <p class="body-copy">Lorem ipsum dolor sit amet, consectetur adipisicing elit. Proin nibh augue, suscipit a, scelerisque sed, lacinia in, mi. Cras vel lorem. Etiam pellentesque aliquetLorem ipsum dolor sit amet, consectetur adipisicing elit. Proin nibh augue, suscipit a, scelerisque sed, lacinia in, mi. Cras vel lorem. Etiam pellentesque aliquetLorem ipsum dolor sit amet, consectetur adipisicing elit. Proin nibh augue, suscipit a, scelerisque sed, lacinia in, mi. Cras vel lorem. Etiam pellentesque aliquetLorem ipsum dolor sit amet, consectetur adipisicing elit. Proin nibh augue, suscipit a, scelerisque sed.</p>
  </main>
  <div class="footer-rule"></div>
</body>
</html>
```